Business Card Design

We are a commercial real estate brokerage in San Francisco, leasing office buildings downtown.
I would like a clean, elegant look. Simple but powerful .

Industry/Entity Type

Business

Contact Information for Business Card

Colin Farrow
lic# 07281549
415.555.0172
colin@tarvo-commercial.example
tarvo-commercial.example

```html
<!DOCTYPE html>
<html lang="en">
<head>
<meta charset="utf-8">
<title>Tarvo Commercial – Business Card</title>
<link rel="stylesheet" href="https://fonts.googleapis.com/css2?family=Figtree:wght@400;600;700&display=swap">
<style>
  :root {
    --page-bg: #e6e7e9;
    --card-bg: #f6f7f8;
    --card-edge: #d4d7dc;
    --brand-blue: #4a5a7a;
    --ink-dark: #2b2d31;
    --ink-mid: #45474b;
    --band: #4b5875;
    --skyline-light: #7a7d82;
    --skyline-dark: #26282b;
  }
  * { box-sizing: border-box; margin: 0; padding: 0; }
  html, body { width: 1200px; height: 970px; overflow: hidden; }
  body {
    background: var(--page-bg);
    font-family: "Figtree", "Helvetica Neue", Arial, sans-serif;
    position: relative;
  }
  .card {
    position: absolute;
    left: 79px; top: 195px;
    width: 1042px; height: 580px;
    background: var(--card-bg);
    border: 1px solid var(--card-edge);
    overflow: hidden;
  }
  .logo-square {
    position: absolute; left: 50px; top: 74px;
    width: 120px; height: 120px;
    background: var(--brand-blue);
  }
  .logo-divider {
    position: absolute; left: 268px; top: 76px;
    width: 3px; height: 120px;
    background: var(--ink-dark);
  }
  .wordmark {
    position: absolute; left: 300px; top: 72px;
    color: var(--brand-blue); font-weight: 700; line-height: 1;
  }
  .wordmark-main { display: block; font-size: 70px; letter-spacing: 1px; }
  .wordmark-sub { display: block; font-size: 31px; letter-spacing: 1.5px; margin-top: 12px; }
  .name {
    position: absolute; left: 50px; top: 280px;
    font-size: 31px; font-weight: 700; color: var(--brand-blue);
  }
  .license {
    position: absolute; left: 50px; top: 360px;
    font-size: 22px; color: var(--ink-mid);
  }
  .contact-list {
    position: absolute; left: 50px; top: 414px;
    list-style: none;
  }
  .contact-list li {
    display: flex; align-items: center; gap: 12px;
    height: 36px; font-size: 22px; color: var(--ink-mid);
  }
  .contact-list svg { width: 22px; height: 22px; fill: var(--ink-dark); flex: none; }
  .contact-list strong { font-weight: 600; color: var(--brand-blue); }
  .skyline {
    position: absolute; left: 559px; top: 297px;
    width: 435px; height: 283px;
    background: linear-gradient(180deg, var(--skyline-light) 0%, var(--skyline-dark) 100%);
  }
  .band { position: absolute; bottom: 0; height: 16px; background: var(--band); }
  .band-left { left: 0; width: 552px; }
  .band-right { left: 998px; right: 0; }
</style>
</head>
<body>
  <section class="card">
    <div class="logo-square"></div>
    <div class="logo-divider"></div>
    <div class="wordmark">
      <span class="wordmark-main">TARVO</span>
      <span class="wordmark-sub">COMMERCIAL</span>
    </div>

    <div class="name">Colin Farrow</div>
    <div class="license">Lic # 07281549</div>

    <ul class="contact-list">
      <li>
        <svg viewBox="0 0 24 24" aria-hidden="true"><path d="M3 9c0-3 4-5 9-5s9 2 9 5v2h-5V9H8v2H3z M6 12h12l2 8H4z"/></svg>
        415.555.0172
      </li>
      <li>
        <svg viewBox="0 0 24 24" aria-hidden="true"><path d="M2 5h20v14H2z M4 7v1l8 5 8-5V7l-8 5z" fill-rule="evenodd"/></svg>
        colin@tarvo-commercial.example
      </li>
      <li>
        <svg viewBox="0 0 24 24" aria-hidden="true"><path d="M12 2a10 10 0 1 0 0 20 10 10 0 0 0 0-20zm0 2a8 8 0 0 1 7.4 5H15l-2-3-3 1 1 3-3 2v3l-3 1A8 8 0 0 1 12 4z"/></svg>
        <span>www.<strong>tarvo-commercial</strong>.example</span>
      </li>
    </ul>

    <div class="skyline" role="img" aria-label="Illustration of downtown office towers skyline"></div>
    <div class="band band-left"></div>
    <div class="band band-right"></div>
  </section>
</body>
</html>
```